File your income taxes and walk away with cash today. direct mailer campaign

We prepare income tax returns. Our slogan is Walk away with cash today! Our marketing edge above our competition is the fact that clients can get up to $5000 the day they file. We also offer notary, payroll, and bookkeeping services. We would like something with cash on the card as well. Quill Ledger Returns is the name of our company and this campaign is actually for a direct mailer to client prospects that make under 25k a year, who will be looking for help preparing their income tax documents but also be looking for cash the same day they file. Our office will begin handing out checks on January 2nd!

Target Market(s)

My target market for this particular piece is Blacks and Hispanics of lower income.

Industry/Entity Type

Finance And Accounting

Font styles to use
Serif
Script

Colors
a54499
b768aa
33a6d7
33b8a4
e667a6
e34197

Requirements
Must have
• Quill Ledger Returns should be written is some form of script, prefer colors of Purple & aqua or Pink and Turquoise. Some form of cash that looks as real as possible.
Nice to have
• Here is our contact info:
• 412 North Caldwell Hammond Parkway
• Dallas, TX 75148
• (281) 555-0374
• www.quillledgerreturns.example
Should not have
• No white people or body parts

```html
<!DOCTYPE html>
<html lang="en">
<head>
<meta charset="utf-8">
<title>Quill Ledger Returns – Direct Mailer</title>
<link rel="stylesheet" href="https://fonts.googleapis.com/css2?family=Great+Vibes&family=Open+Sans:wght@400;600;700&display=swap">
<style>
  :root {
    --stage: #1f6f99;
    --card: #ffffff;
    --pink: #e667a6;
    --purple: #a54499;
    --purple-deep: #7d3a86;
    --aqua: #33a6d7;
    --aqua-deep: #2a93c4;
    --ink-light: #ffffff;
    --rule: #b9b9b9;
    --muted: #8a8a8a;
    --script: "Great Vibes", cursive;
    --sans: "Open Sans", Arial, sans-serif;
  }
  * { box-sizing: border-box; margin: 0; padding: 0; }
  html, body { width: 1066px; height: 1200px; overflow: hidden; }
  body { background: var(--stage); position: relative; font-family: var(--sans); }

  .card { position: absolute; left: 218px; width: 632px; background: var(--card); overflow: hidden; }
  .card--front { top: 83px; height: 491px; }
  .card--back { top: 624px; height: 492px; }

  /* Front */
  .front-visual {
    position: absolute; left: 0; top: 0; width: 380px; height: 413px;
    background: linear-gradient(100deg, #cdb7d2 0%, #e6dcc0 40%, #f1ecd6 65%, #ffffff 100%);
  }
  .brand-title {
    position: absolute; right: 40px; top: 30px; width: 320px;
    font-family: var(--script); font-weight: 400; color: var(--pink);
    font-size: 72px; line-height: 0.9; text-align: right;
  }
  .brand-title span { display: block; }
  .brand-title span:nth-child(2) { margin-right: 14px; }
  .brand-title span:nth-child(3) { margin-right: 40px; }

  .practitioner {
    font-family: var(--script); color: var(--purple);
    font-size: 29px; line-height: 1.05;
  }
  .card--front .practitioner { position: absolute; right: 56px; top: 272px; text-align: right; }

  .contact-bar {
    position: absolute; left: 19px; top: 413px; width: 594px; height: 58px;
    border-radius: 10px;
    background: linear-gradient(105deg, var(--aqua) 0 34%, var(--aqua-deep) 34% 36%, var(--aqua) 36% 72%, var(--aqua-deep) 72% 74%, var(--aqua) 74%);
    color: var(--ink-light); display: flex; align-items: center;
  }
  .contact-item { display: flex; align-items: flex-start; gap: 5px; font-size: 10.5px; line-height: 1.45; white-space: nowrap; }
  .contact-item svg { flex: none; margin-top: 2px; }
  .contact-item--phone { font-size: 17px; align-items: center; }
  .contact-item--phone svg { margin-top: 0; }
  .contact-bar .contact-item--phone { margin-left: 18px; width: 140px; }
  .contact-bar .contact-item--address { width: 218px; }
  .contact-bar .contact-item--web { margin-left: 6px; }

  /* Back */
  .back-header {
    position: absolute; left: 0; top: 0; width: 387px; height: 168px;
    background: linear-gradient(90deg, #e9ebec 0%, #f4f5f5 60%, #fafafa 100%);
  }
  .back-photo {
    position: absolute; left: 0; top: 0; width: 160px; height: 168px;
    background: linear-gradient(160deg, #c9cfd3 0%, #8e8f8c 55%, #5b5d5c 100%);
  }
  .card--back .practitioner { position: absolute; left: 160px; top: 32px; width: 227px; text-align: center; font-size: 27px; }
  .back-email { position: absolute; left: 160px; top: 126px; width: 227px; text-align: center; font-size: 11px; color: var(--purple); white-space: nowrap; }

  .offer-panel {
    position: absolute; left: 0; top: 168px; width: 387px; height: 210px;
    background: var(--aqua); color: var(--ink-light); padding: 16px 20px 0 30px;
  }
  .offer-headline { font-size: 22px; font-weight: 600; letter-spacing: -0.2px; }
  .offer-body { margin-top: 8px; font-size: 14.5px; font-weight: 600; line-height: 1.36; }
  .slogan { margin-top: 6px; margin-left: -6px; font-family: var(--script); font-size: 30px; }

  .info-band {
    position: absolute; left: 0; top: 378px; width: 387px; height: 59px;
    background: linear-gradient(90deg, var(--purple-deep), var(--purple));
    border-radius: 0 0 8px 0; color: var(--ink-light);
    display: flex; align-items: center;
  }
  .info-band .contact-item--phone { margin-left: 20px; width: 140px; }

  .stamp-box { position: absolute; left: 546px; top: 45px; width: 57px; height: 57px; border: 1px solid var(--rule); }
  .address-line { position: absolute; left: 419px; width: 184px; height: 1px; background: var(--rule); }
  .address-line--1 { top: 178px; }
  .address-line--2 { top: 215px; }
  .address-line--3 { top: 255px; }
  .address-line--4 { top: 294px; }
  .footer-url { position: absolute; right: 29px; top: 448px; font-size: 7.5px; color: var(--muted); letter-spacing: 0.6px; }
</style>
</head>
<body>

<section class="card card--front">
  <div class="front-visual" role="img" aria-label="Photo of an alarm clock with a Tax time sticky note and dollar bills falling from above"></div>

  <h1 class="brand-title"><span>Quill</span><span>Ledger</span><span>Returns</span></h1>

  <p class="practitioner">Rosalind Quill<br>Manager,<br>Tax Practitioner</p>

  <div class="contact-bar">
    <div class="contact-item contact-item--phone">
      <svg width="10" height="14" viewBox="0 0 10 14"><rect x="1" y="0.5" width="8" height="13" rx="1.5" fill="none" stroke="#fff"/></svg>
      (281) 555-0374
    </div>
    <div class="contact-item contact-item--address">
      <svg width="8" height="11" viewBox="0 0 8 11"><path d="M4 0a4 4 0 0 1 4 4c0 3-4 7-4 7S0 7 0 4a4 4 0 0 1 4-4z" fill="#fff"/><circle cx="4" cy="4" r="1.5" fill="#33a6d7"/></svg>
      <span>412 North Caldwell Hammond Parkway,<br>Dallas, TX 75148</span>
    </div>
    <div class="contact-item contact-item--web">
      <svg width="10" height="26" viewBox="0 0 10 26"><circle cx="5" cy="5" r="4.2" fill="none" stroke="#fff" stroke-width="1.4"/><path d="M1 5h8M5 1v8" stroke="#fff"/><rect x="0.5" y="17" width="9" height="6" fill="#fff"/><path d="M0.5 17l4.5 3.5 4.5-3.5" fill="none" stroke="#33a6d7"/></svg>
      <span>www.quillledgerreturns.example<br>rosalind@quillledgerreturns.example</span>
    </div>
  </div>
</section>

<section class="card card--back">
  <div class="back-header">
    <div class="back-photo" role="img" aria-label="Photo of a smiling tax preparer wearing a headset at an office desk"></div>
    <p class="practitioner">Rosalind Quill<br>Manager,<br>Tax Practitioner</p>
    <p class="back-email">rosalind@quillledgerreturns.example</p>
  </div>

  <div class="offer-panel">
    <h2 class="offer-headline">Upto $5000 same day you file!</h2>
    <p class="offer-body">15 years of tax experience! we will get your maximum refund! Submit documents securely from home! Hasta $5000 Hoy! 15 anos de experiencia en impuestos! Obtendremos su reembolso maximo!</p>
    <p class="slogan">Walk away with cash today!</p>
  </div>

  <div class="info-band">
    <div class="contact-item contact-item--phone">
      <svg width="11" height="11" viewBox="0 0 11 11"><path d="M2 0.5l2 2.2-1 1.3c.7 1.6 2 2.9 3.6 3.6l1.3-1 2.2 2-1.3 1.9C4.5 10.3.7 6.5.2 2z" fill="#fff"/></svg>
      (281) 555-0374
    </div>
    <div class="contact-item contact-item--address">
      <svg width="7" height="10" viewBox="0 0 8 11"><path d="M4 0a4 4 0 0 1 4 4c0 3-4 7-4 7S0 7 0 4a4 4 0 0 1 4-4z" fill="#fff"/><circle cx="4" cy="4" r="1.5" fill="#8c3f90"/></svg>
      <span>412 North Caldwell Hammond Parkway,<br>Dallas, TX 75148</span>
    </div>
  </div>

  <div class="stamp-box"></div>
  <div class="address-line address-line--1"></div>
  <div class="address-line address-line--2"></div>
  <div class="address-line address-line--3"></div>
  <div class="address-line address-line--4"></div>

  <p class="footer-url">www.quillledgerreturns.example</p>
</section>

</body>
</html>
```